Responsive WordPress website for medical therapy practice consulting business.

We need both design and website for responsive Wordpress website. The use of Quorvel theme is preferred when considering the design (not required).
Site must be designed for 1920px width and fully responsive.
See full scope of the project below.

DESIGN:
Design a full screen layout using images and parallax movement where appropriate.
Easy to use navigation for desktop and hamburger style navigation for mobile devices.
Create an original design for the home, sub-page template.
Create a responsive website using common desktop breakpoints 1920, 1366, 1280 1024 as well as mobile devices.
Color scheme should use soft or pastel color avoiding reds.
Design will take inspiration from logo design and color scheme.
Large “Hero slider” may be employed to striking visual interest.
The website will focus the content on the Homepage mission statement, What We Do and How to Reach Us, content.
Website Footer Information: Include content for Privacy Policy and Terms of Use, address and copyright information.

DEVELOPMENT NOTES:

WordPress content management platform will be used .

Responsive grid will be used to properly display website content on all devices including mobile, laptop and desktop at standard breakpoints.

Social Media links to LinkedIn and Twitter

Google Analytics and Search Console integration – allows tracking of visitors and in-depth search data, indexing and performance.

Yoast Basic SEO – basic setup and integration is included in the proposal. This includes creating SEO friendly page titles, search descriptions and best practices for heading and image tags.

508 & ADA compliance

PAGE LIST:
The following pages are a list of current websites pages. These are used as a guideline for developing the proposal and can be changed to reflect content:

NAVIGATION LINKS:

HOME

· Featuring the new logo, the home page will display Brightmoor Care Partners’s message, services, and contact information.
· The navigation will be prominent, intuitive and easy to use, allowing to find information quickly.
· Parallax scrolling will provide a cool modern visual effect without being overbearing.

====================================================

ABOUT US –

· History
· Bios
· Links

SERVICES

· Business Consultancy service

CONTACT US – This section will present ways for viewers to reach out either by phone, email.

· Google map of office locations.
· Business information
a. Locations
b. Address
c. Phone
d. Fax
e. Email

FOOTER LINKS – Additional information for legal or usage claims, company info and contact info.

· Copyright information
· Links to CONTACT
· Social Media
· Disclaimer
· Privacy policy
· Terms of use

```html
<!DOCTYPE html>
<html lang="en">
<head>
<meta charset="utf-8">
<title>Brightmoor Care Partners — Home</title>
<link rel="stylesheet" href="https://fonts.googleapis.com/css2?family=Arimo:wght@400;700&family=Montserrat:wght@400;700&display=swap">
<style>
:root{
  --page:#ffffff;
  --brand:#1a7fc4;
  --brand-dark:#1f5fa8;
  --button:#1e7ff0;
  --text:#555a60;
  --muted:#7a7f85;
  --overlay:rgba(104,124,196,.82);
  --violet-a:#8f86c4;
  --violet-b:#a58ab8;
  --band-a:#4d9fe0;
  --band-b:#5aa8e6;
  --footer:#232323;
  --footer-bottom:#1b1b1b;
  --footer-text:#8d8d8d;
  --footer-line:#3a3a3a;
}
*{box-sizing:border-box;margin:0;padding:0}
html,body{width:1200px;height:1200px;overflow:hidden;background:var(--page)}
body{font-family:"Arimo",Arial,sans-serif;color:var(--text);position:relative}
.site{position:absolute;left:346px;top:0;width:635px;height:1500px;transform:scale(.8);transform-origin:0 0}
.abs{position:absolute}

/* header + hero */
.hero-photo{left:0;top:0;width:635px;height:366px;background:linear-gradient(100deg,#e8e2d8 0%,#d9cbb5 35%,#cfd3d6 60%,#8f9496 100%)}
.hero-rule{left:2px;top:366px;width:631px;height:2px;background:var(--brand)}
.header{left:0;top:0;width:635px;height:62px;background:rgba(255,255,255,.88)}
.brand{left:48px;top:22px;display:flex;align-items:center;gap:8px;font-size:15px;font-weight:700;color:var(--brand-dark)}
.brand-mark{width:12px;height:12px;background:var(--brand-dark)}
.nav{left:355px;top:24px;display:flex;gap:14px;font-size:12.5px;color:#333}
.nav a{color:#333;text-decoration:none;line-height:21px}
.nav .current{border:2px solid var(--brand);padding:0 8px}
.slide-box{left:141px;top:178px;width:349px;height:144px;background:var(--overlay);text-align:center;color:#fff}
.slide-kicker{margin-top:20px;font-size:28px;line-height:30px}
.slide-title{font-size:40px;line-height:42px;letter-spacing:1px}
.slide-btn{display:inline-block;margin-top:14px;border:1px solid #fff;width:104px;height:21px;font-size:9.5px;line-height:19px;color:#fff}
.arrow{width:22px;height:22px}

/* about */
.about-photo{left:35px;top:425px;width:212px;height:257px;background:linear-gradient(180deg,#f2f2f2,#e3e6ea 60%,#cdd3da)}
.section-title{font-size:18px;font-weight:400;color:var(--brand);letter-spacing:.3px}
.about-title{left:271px;top:411px}
.about-copy{left:270px;top:450px;width:330px;font-size:9.5px;line-height:12.7px;color:var(--text)}
.about-copy p+p{margin-top:12px}
.read-more{left:277px;top:604px;width:48px;height:18px;background:var(--button);color:#fff;font-size:6.5px;line-height:18px;text-align:center}
.divider{left:224px;top:709px;width:407px;height:1px;background:#e2e2e2}

/* services */
.services-panel{left:0;top:709px;width:224px;height:332px;background:linear-gradient(135deg,var(--violet-a),var(--violet-b));color:#fff;text-align:center}
.services-panel h2{font-weight:400;font-size:19px;margin-top:134px}
.services-panel p{margin:14px auto 0;width:160px;font-size:9.5px;line-height:14.6px;font-weight:700}
.service-title{left:224px;top:717px;width:407px;text-align:center}
.service{width:110px;text-align:center}
.service svg{display:block;margin:0 auto}
.service h3{margin-top:8px;font-weight:400;font-size:10px;color:var(--muted);letter-spacing:.3px}
.service p{margin-top:5px;font-size:7.8px;line-height:10px;color:var(--muted)}

/* testimonial */
.band{left:0;top:1070px;width:635px;height:200px;background:linear-gradient(90deg,var(--band-a),var(--band-b) 50%,#6db2e8)}
.avatar{left:262px;top:1077px;width:86px;height:86px;border-radius:50%;background:#fff}
.quote{left:95px;top:1180px;width:440px;text-align:center;color:#fff;font-size:6px;line-height:8px;font-weight:700}
.quote-name{left:0;top:1225px;width:635px;text-align:center;color:#fff;font-size:6px;font-weight:700}

/* footer */
.footer{left:2px;top:1270px;width:629px;height:188px;background:var(--footer);font-family:"Montserrat",Arial,sans-serif;color:var(--footer-text)}
.footer-col{position:absolute;top:33px}
.footer h4{font-size:6.5px;color:#fff;letter-spacing:.5px}
.footer-about{left:67px;width:155px}
.footer-about p{margin-top:20px;font-size:6.2px;line-height:12px}
.footer-sep{position:absolute;top:32px;width:1px;height:132px;background:var(--footer-line)}
.posts{left:253px;width:156px}
.posts ul{list-style:none;margin-top:14px}
.posts li{font-size:6px;height:24.5px;line-height:24px;border-bottom:1px solid var(--footer-line);padding-left:14px;position:relative}
.posts li::before{content:"›";position:absolute;left:3px}
.tags{left:438px;width:150px}
.tags div{margin-top:16px;display:flex;flex-wrap:wrap;gap:6px}
.tags span{border:1px solid #4a4a4a;font-size:4.6px;padding:5px 8px;color:#bbb;text-transform:uppercase}
.footer-bottom{left:2px;top:1458px;width:629px;height:42px;background:var(--footer-bottom);text-align:center;font-family:"Montserrat",Arial,sans-serif;font-size:6px;line-height:42px;color:#777}
</style>
</head>
<body>
<div class="site">
  <div class="abs hero-photo" role="img" aria-label="Photo of a therapist in conversation with a client"></div>
  <div class="abs hero-rule"></div>
  <header class="abs header">
    <div class="abs brand"><span class="brand-mark"></span>Brightmoor Care Partners</div>
    <nav class="abs nav"><a class="current" href="#">Home</a><a href="#">About Us</a><a href="#">Services</a><a href="#">Contact US</a></nav>
  </header>
  <svg class="abs arrow" style="left:36px;top:214px" viewBox="0 0 22 22"><circle cx="11" cy="11" r="10" fill="rgba(255,255,255,.25)" stroke="#fff" stroke-width="1.5"/><path d="M13 6 L8 11 L13 16" fill="none" stroke="#fff" stroke-width="2"/></svg>
  <svg class="abs arrow" style="left:564px;top:214px" viewBox="0 0 22 22"><circle cx="11" cy="11" r="10" fill="rgba(255,255,255,.25)" stroke="#fff" stroke-width="1.5"/><path d="M9 6 L14 11 L9 16" fill="none" stroke="#fff" stroke-width="2"/></svg>
  <div class="abs slide-box">
    <div class="slide-kicker">A Whole New</div>
    <div class="slide-title">THERAPHY</div>
    <span class="slide-btn">Discover More ➤</span>
  </div>

  <div class="abs about-photo" role="img" aria-label="Portrait of a senior doctor in a white coat"></div>
  <h2 class="abs section-title about-title">ABOUT US</h2>
  <div class="abs about-copy">
    <p>This is Larkfield's version of Lorem Ipsum. Proin gravida nibh vel velit auctor aliquet. Aenean sollicitudin, lorem quis bibendum auctor, nisi elit consequat ipsum, nec sagittis sem nibh id elit. Duis sed odio sit amet nibh vulputate cursus a sit amet mauris. Morbi accumsan ipsum velit. Nam nec tellus a odio tincidunt auctor a ornare odio. Sed non mauris vitae erat cons</p>
    <p>amet nibh vulputate cursus a sit amet mauris. Morbi accumsan ipsum velit. Nam nec tellus a odio tincidunt auctor a ornare odio. Sed non mauris vitae erat cons</p>
  </div>
  <div class="abs read-more">Read More</div>
  <div class="abs divider"></div>

  <section class="abs services-panel" role="img" aria-label="Softly tinted photo of a smiling therapist">
    <h2>OUR SERVICES</h2>
    <p>This is Larkfield's version of Lorem Ipsum. Proin gravida nibh vel velit auctor aliquet. Aenean soinceptos himenaeos. Mauris in erat justo. Nullam ac urna eu felis dapibus</p>
  </section>
  <h2 class="abs section-title service-title">OUR SERVICE</h2>

  <div class="abs service" style="left:227px;top:753px"><svg width="18" height="18" viewBox="0 0 18 18"><circle cx="9" cy="9" r="8" fill="none" stroke="var(--brand)" stroke-width="1.5"/><path d="M9 5v8M5 9h8" stroke="var(--brand)" stroke-width="1.8"/></svg><h3>SERVICES</h3><p>This is Larkfield's version of Lorem Ipsum. Proin gravida nibh vel velit vsed fermentum feugiat, vneque. Suspendisse in orci enim.</p></div>
  <div class="abs service" style="left:367px;top:753px"><svg width="18" height="18" viewBox="0 0 18 18"><circle cx="9" cy="9" r="8" fill="none" stroke="var(--brand)" stroke-width="1.5"/><path d="M9 5v8M5 9h8" stroke="var(--brand)" stroke-width="1.8"/></svg><h3>SERVICES</h3><p>This is Larkfield's version of Lorem Ipsum. Proin gravida nibh vel velit vsed fermentum feugiat, vneque. Suspendisse in orci enim.</p></div>
  <div class="abs service" style="left:503px;top:753px"><svg width="18" height="18" viewBox="0 0 18 18"><circle cx="9" cy="9" r="8" fill="none" stroke="var(--brand)" stroke-width="1.5"/><path d="M9 5v8M5 9h8" stroke="var(--brand)" stroke-width="1.8"/></svg><h3>SERVICES</h3><p>This is Larkfield's version of Lorem Ipsum. Proin gravida nibh vel velit vsed fermentum feugiat, vneque. Suspendisse in orci enim.</p></div>
  <div class="abs service" style="left:227px;top:895px"><svg width="18" height="18" viewBox="0 0 18 18"><circle cx="9" cy="9" r="8" fill="none" stroke="var(--brand)" stroke-width="1.5"/><path d="M9 5v8M5 9h8" stroke="var(--brand)" stroke-width="1.8"/></svg><h3>SERVICES</h3><p>This is Larkfield's version of Lorem Ipsum. Proin gravida nibh vel velit vsed fermentum feugiat, vneque. Suspendisse in orci enim.</p></div>
  <div class="abs service" style="left:367px;top:895px"><svg width="18" height="18" viewBox="0 0 18 18"><circle cx="9" cy="9" r="8" fill="none" stroke="var(--brand)" stroke-width="1.5"/><path d="M9 5v8M5 9h8" stroke="var(--brand)" stroke-width="1.8"/></svg><h3>SERVICES</h3><p>This is Larkfield's version of Lorem Ipsum. Proin gravida nibh vel velit vsed fermentum feugiat, vneque. Suspendisse in orci enim.</p></div>
  <div class="abs service" style="left:503px;top:895px"><svg width="18" height="18" viewBox="0 0 18 18"><circle cx="9" cy="9" r="8" fill="none" stroke="var(--brand)" stroke-width="1.5"/><path d="M9 5v8M5 9h8" stroke="var(--brand)" stroke-width="1.8"/></svg><h3>SERVICES</h3><p>This is Larkfield's version of Lorem Ipsum. Proin gravida nibh vel velit vsed fermentum feugiat, vneque. Suspendisse in orci enim.</p></div>

  <section class="abs band" role="img" aria-label="Blue tinted photo of a doctor speaking with a patient"></section>
  <div class="abs avatar"></div>
  <svg class="abs" style="left:81px;top:1119px" width="18" height="18" viewBox="0 0 18 18"><circle cx="9" cy="9" r="8" fill="none" stroke="#fff" stroke-width="1.5"/><path d="M11 5 L7 9 L11 13" fill="none" stroke="#fff" stroke-width="1.8"/></svg>
  <svg class="abs" style="left:545px;top:1119px" width="18" height="18" viewBox="0 0 18 18"><circle cx="9" cy="9" r="8" fill="none" stroke="#fff" stroke-width="1.5"/><path d="M7 5 L11 9 L7 13" fill="none" stroke="#fff" stroke-width="1.8"/></svg>
  <p class="abs quote">This is Larkfield's version of Lorem Ipsum. Proin gravida nibh vel velit auctor aliquet. Aenean sollicitudin, lorem quis bibendum auctor, nisi elit consequat ipsum, nec sagittis sem nibh id elit. Duis sed odio sit amet nibh vulputate cursus a sit amet mauris. Morbi accumsan ipsum velit. Nam nec tellus a odio tincidunt auctor a ornare odio. Sed non mauris vitae erat consequat auctor tincidunt auctor a ornare odio. Sed non mauris vitae erat consequat auctor</p>
  <p class="abs quote-name">Marla Quince</p>

  <footer class="abs footer">
    <div class="footer-col footer-about"><h4>ABOUT US</h4><p>A wonderful serenity has taken possession of my entire soul, like these sweet mornings of spring which I enjoy with my whole heart. I am alone, and feel the charm of existence in this spot, which was created for the bliss of</p></div>
    <div class="footer-sep" style="left:238px"></div>
    <div class="footer-col posts"><h4>RECENT POSTS</h4><ul><li>Wonderful serenity has taken</li><li>In my soul and absorb its power</li><li>I hear the buzz of the little</li><li>And heaven and earth seem to dwell</li></ul></div>
    <div class="footer-sep" style="left:423px"></div>
    <div class="footer-col tags"><h4>TAG CLOUD</h4><div><span>Business</span><span>Conference</span><span>Gadgets</span><span>Identity</span><span>Logo</span><span>Photography</span><span>Time</span><span>Trips</span><span>Works</span><span>Work space</span></div></div>
  </footer>
  <div class="abs footer-bottom">COPYRIGHT 2020 FERNWICK THEMES, ALL RIGHT RESERVED</div>
</div>
</body>
</html>
```